DL flyer design with creative use of typography.

Brief: Design a double sided DL brochure to advertise my real estate agency sales service. I like to look different from our competitors who are typically corporate look real estate agents.
The brochure will be delivered to houses located in a high quality, housing estate surrounded by a Marina (i.e. Yachts, boardwalks, ocean)

The design should communicate retro./nostalgia with a coastal/yachting marina theme and creative use of typography. Illustrations/illustrative style is encouraged.

PLEASE WATCH Our company video commercial: https://www.vidplexo.com/watch?v=kTbLqZ3mVxR

Our website: http://www.harbenrealestate.com.au

Our facebook page: https://www.friendloop.com/thecorvanes

Content and example images have been uploaded.
Updates

Target Market(s)

We have two target markets

1. Couples aged 35-49 (parents and homebuilders)

2. Singles and Couples aged 50-69 years old (empty nesters and retirees). They do not like to feel like they are old

Industry/Entity Type

Real Estate Agent

Font styles to use
Decorative

Requirements
Must have
• The design should communicate retro./nostalgia with a coastal/yachting marina theme and creative use of typography. Illustrations/illustrative style is encouraged.
• Use pre-written content and my image (supplied).
• Use some/all of the sold property images (supplied)
Should not have
• Corporate feel

```html
<!DOCTYPE html>
<html lang="en">
<head>
<meta charset="utf-8">
<title>Harben Real Estate – DL Flyer</title>
<link href="https://fonts.googleapis.com/css2?family=Roboto+Condensed:ital,wght@0,400;0,700;1,400;1,700&family=Exo+2:ital,wght@1,800&family=Kalam:wght@400;700&family=Griffy&family=Homemade+Apple&family=Merienda:wght@400;700&display=swap" rel="stylesheet">
<style>
  :root{
    --navy:#1f3a8a;
    --royal:#2e4aa0;
    --bright:#3a5bc0;
    --ink:#2a2a2a;
    --sea-deep:#1c3b7e;
    --sea:#3f72ad;
    --sky:#eef2fa;
    --sand:#f6d8c4;
    --white:#ffffff;
    --page:#e9e9e9;
    --sold-band:rgba(86,92,178,.78);
  }
  *{margin:0;padding:0;box-sizing:border-box}
  html,body{width:1200px;height:1200px;overflow:hidden;background:var(--page)}
  .canvas{position:relative;width:1200px;height:1200px}
  .panel{position:absolute;top:82px;width:460px;height:1035px;background:var(--white);overflow:hidden;box-shadow:0 4px 14px rgba(0,0,0,.18)}
  .front{left:110px}
  .back{left:630px}
  .abs{position:absolute}
  .body-font{font-family:"Roboto Condensed",sans-serif}

  /* front – header */
  .sea-top,.sea-bottom{position:absolute;left:0}
  .sea-top{top:0}
  .sea-bottom{top:590px}
  .brand{left:32px;top:32px;color:var(--navy);font-family:"Roboto Condensed",sans-serif;font-weight:700;text-align:center;line-height:1}
  .brand .name{font-size:36px;letter-spacing:1px}
  .brand .sub{font-size:12px;letter-spacing:3px;margin-top:4px}
  .brand .tag{font-size:9px;letter-spacing:3px;margin-top:3px}
  .why{left:200px;top:46px;font-family:"Kalam",cursive;font-size:27px;color:var(--ink)}
  .talk{right:24px;top:78px;font-family:"Exo 2",sans-serif;font-style:italic;font-weight:800;font-size:40px;color:var(--bright)}
  .selling{right:24px;top:128px;text-align:right;color:var(--white);font-family:"Roboto Condensed",sans-serif;font-style:italic;line-height:1}
  .selling .line1{font-size:23px}
  .selling .line2{font-family:"Exo 2",sans-serif;font-size:31px;font-weight:800;margin-top:4px}

  /* front – statements */
  .own-box{left:30px;top:218px;width:220px;height:76px;background:var(--royal);color:var(--white);font-family:"Roboto Condensed",sans-serif;font-size:28px;line-height:1;text-align:center;padding-top:8px}
  .own-place{left:30px;top:294px;width:220px;text-align:center;font-family:"Roboto Condensed",sans-serif;font-style:italic;font-weight:700;font-size:20px;color:var(--bright);display:flex;align-items:center;gap:6px}
  .own-place::before,.own-place::after{content:"";flex:1;border-top:2px dotted var(--ink)}
  .benefit{left:30px;top:318px;width:220px;height:76px;border:2px dotted var(--ink);border-top:none;text-align:center;color:var(--ink);line-height:1.05;padding-top:4px}
  .benefit .a{font-family:"Kalam",cursive;font-weight:700;font-size:22px}
  .benefit .b{font-family:"Roboto Condensed",sans-serif;font-size:18px}
  .benefit .c{font-family:"Kalam",cursive;font-size:17px;text-transform:uppercase}

  .passion{left:268px;top:228px;width:180px;text-align:center;color:var(--ink);font-family:"Roboto Condensed",sans-serif;font-size:20px;line-height:1.2}
  .passion .lead{font-style:italic;font-weight:700;font-size:27px;color:var(--bright)}
  .passion .hand{font-family:"Kalam",cursive;font-weight:700;font-size:24px}
  .passion .caps{font-weight:700;letter-spacing:1px}

  .marketing{left:20px;top:420px;width:190px;text-align:center;color:var(--ink);line-height:1.1}
  .marketing .a{font-family:"Roboto Condensed",sans-serif;font-size:21px;color:var(--bright)}
  .marketing .b{font-family:"Griffy",cursive;font-size:23px}
  .marketing .c{font-family:"Griffy",cursive;font-size:24px}
  .marketing .d{font-family:"Homemade Apple",cursive;font-size:16px;margin-top:4px}
  .marketing .e{font-family:"Homemade Apple",cursive;font-size:24px;margin-top:2px}

  .care-shape{left:222px;top:418px}
  .care{left:232px;top:428px;width:200px;text-align:center;color:var(--white);line-height:1.1}
  .care .lead{font-family:"Roboto Condensed",sans-serif;font-style:italic;font-weight:700;font-size:27px}
  .care .b{font-family:"Roboto Condensed",sans-serif;font-size:20px}
  .care .c{font-family:"Kalam",cursive;font-weight:700;font-size:23px}
  .care .d{font-family:"Kalam",cursive;font-size:17px;text-transform:uppercase}

  /* front – agent */
  .portrait{left:40px;top:650px;width:112px;height:112px;border-radius:50%;background:radial-gradient(circle at 50% 40%,#d9b89c 0,#a88d74 38%,#2d3758 70%,#1d2540 100%);border:3px solid rgba(255,255,255,.7)}
  .agent-name{left:176px;top:636px;font-family:"Exo 2",sans-serif;font-style:italic;font-weight:800;font-size:35px;color:var(--bright)}
  .agent-role{left:178px;top:684px;font-family:"Roboto Condensed",sans-serif;font-size:17px;line-height:1.05;color:var(--ink)}
  .agent-diploma{left:178px;top:724px;font-family:"Roboto Condensed",sans-serif;font-weight:700;font-size:17px;color:var(--ink)}
  .years{left:140px;top:748px;width:170px;height:56px;border:3px solid var(--royal);background:var(--white);transform:rotate(-3deg);font-family:"Exo 2",sans-serif;font-style:italic;font-weight:800;font-size:33px;color:var(--royal);text-align:center;line-height:50px}
  .ribbon{left:14px;top:796px}
  .ribbon-text{left:108px;top:818px;width:240px;text-align:center;transform:rotate(-5deg);font-family:"Roboto Condensed",sans-serif;font-style:italic;font-weight:700;font-size:15px;color:var(--white)}

  /* front – contact */
  .contact{left:110px;top:870px;list-style:none;font-family:"Merienda",cursive;font-size:15px;color:var(--ink)}
  .contact li{display:flex;align-items:center;gap:10px;height:27px}
  .contact li:nth-child(2){padding-left:26px}
  .contact li:nth-child(3),.contact li:nth-child(4){padding-left:0}
  .contact li:nth-child(5){margin-left:-52px}
  .contact .ico{width:22px;height:22px;flex:none}
  .contact .web{color:var(--bright);font-weight:700}

  /* back */
  .photo{position:absolute}
  .hero{left:0;top:0;width:460px;height:322px;background:linear-gradient(180deg,#4c5ea8 0%,#8d9fd0 30%,#b6b0b6 48%,#6b5a52 60%,#8a8e9c 78%,#a7a9b3 100%)}
  .sold-band{left:0;top:216px;width:460px;height:81px;background:var(--sold-band);color:var(--white);font-family:"Roboto Condensed",sans-serif;font-size:70px;text-align:center;line-height:81px}
  .p-deck{left:0;top:331px;width:192px;height:290px;background:linear-gradient(180deg,#8fb3df 0%,#cfdff0 40%,#7e9fb0 48%,#d6c09d 58%,#9b9a9a 80%,#dadada 100%)}
  .p-dusk{left:200px;top:331px;width:260px;height:290px;background:linear-gradient(180deg,#5c86c6 0%,#e7b6a6 28%,#6b7a4f 50%,#c9b49a 70%,#b8b1aa 100%)}
  .p-lawn{left:0;top:631px;width:460px;height:207px;background:linear-gradient(180deg,#9cc1ea 0%,#c7dcf2 30%,#8c7272 50%,#5f8a3c 66%,#82ab4c 100%)}
  .p-room{left:0;top:848px;width:226px;height:187px;background:linear-gradient(180deg,#f2f2f0 0%,#e8e7e3 45%,#2b2b2b 62%,#3a3a3a 100%)}
  .p-drive{left:234px;top:848px;width:226px;height:187px;background:linear-gradient(180deg,#5a8fd0 0%,#b7d0ec 30%,#4b7a3a 55%,#a59077 75%,#7f9b56 100%)}
</style>
</head>
<body>
<div class="canvas">

  <!-- FRONT -->
  <section class="panel front" aria-label="Flyer front">
    <svg class="sea-top" width="460" height="240" viewBox="0 0 460 240" role="img" aria-label="Photo of calm blue ocean under a pale sky">
      <defs>
        <linearGradient id="seaTop" x1="0" y1="0" x2="0" y2="1">
          <stop offset="0" stop-color="#f7f9fd"/>
          <stop offset="0.28" stop-color="#dde5f3"/>
          <stop offset="0.4" stop-color="#6f97c6"/>
          <stop offset="0.7" stop-color="#2f5d9d"/>
          <stop offset="1" stop-color="#1c3b7e"/>
        </linearGradient>
      </defs>
      <path d="M0 0H460V198C400 214 340 186 270 204S110 228 0 212Z" fill="url(#seaTop)"/>
    </svg>

    <div class="abs brand">
      <div class="name">HARBEN</div>
      <div class="sub">REAL ESTATE</div>
      <div class="tag">AGENTS</div>
    </div>
    <div class="abs why">Why You Should</div>
    <div class="abs talk">Talk To Dean</div>
    <div class="abs selling">
      <div class="line1">If You Are Selling In</div>
      <div class="line2">Kestrel Cove</div>
    </div>

    <div class="abs own-box">I live in &amp; own<br>real estate in</div>
    <div class="abs own-place">Kestrel Cove.</div>
    <div class="abs benefit">
      <div class="a">Benefit from my</div>
      <div class="b">expert local knowledge &amp;</div>
      <div class="c">Body Corporate Expertise.</div>
    </div>

    <div class="abs passion">
      <div class="lead">I believe</div>
      <div>that passion</div>
      <div>and attention</div>
      <div class="hand">to detail</div>
      <div>makes all the</div>
      <div class="caps">DIFFERENCE.</div>
    </div>

    <div class="abs marketing">
      <div class="a">I know that my</div>
      <div class="b">CREATIVE MARKETING</div>
      <div class="c">abilities get</div>
      <div class="d">the best results</div>
      <div class="e">every time.</div>
    </div>

    <svg class="abs care-shape" width="222" height="160" viewBox="0 0 222 160">
      <path d="M6 6L214 0L219 20L216 70L221 120L214 154L120 158L8 152L2 110L7 60L0 20Z" fill="#2e4aa0"/>
    </svg>
    <div class="abs care">
      <div class="lead">I believe</div>
      <div class="b">in looking after</div>
      <div class="b">people &amp;</div>
      <div class="c">making things</div>
      <div class="d">simple and stress free.</div>
    </div>

    <svg class="sea-bottom" width="460" height="190" viewBox="0 0 460 190" role="img" aria-label="Photo of a sunset coastline with soft peach sky over blue water">
      <defs>
        <linearGradient id="seaBottom" x1="0" y1="0" x2="0" y2="1">
          <stop offset="0" stop-color="#f6d8c4"/>
          <stop offset="0.25" stop-color="#9fc0de"/>
          <stop offset="0.6" stop-color="#4f86bd"/>
          <stop offset="1" stop-color="#dce9f4"/>
        </linearGradient>
      </defs>
      <path d="M0 20C80 0 150 22 230 12S380 2 460 16V150C380 172 300 140 230 158S90 178 0 160Z" fill="url(#seaBottom)"/>
    </svg>

    <div class="abs portrait" role="img" aria-label="Portrait photo of the agent in a suit"></div>
    <div class="abs agent-name">Dean Halloway</div>
    <div class="abs agent-role">Licenced real estate agent and<br>body corporate manager</div>
    <div class="abs agent-diploma">Diploma of Art (Graphic Art)</div>

    <svg class="abs ribbon" width="432" height="84" viewBox="0 0 432 84">
      <path d="M0 40L70 24L82 62L14 78L24 58Z" fill="#1f3a8a"/>
      <path d="M432 40L362 24L350 62L418 78L408 58Z" fill="#1f3a8a"/>
      <path d="M62 26Q216 -6 370 26L358 66Q216 34 74 66Z" fill="#2e4aa0"/>
      <path d="M70 33Q216 3 362 33M66 59Q216 27 366 59" stroke="#ffffff" stroke-width="1.5" stroke-dasharray="6 4" fill="none"/>
    </svg>
    <div class="abs years">10+ years'</div>
    <div class="abs ribbon-text">Experience Selling Real Estate</div>

    <ul class="abs contact">
      <li>
        <svg class="ico" viewBox="0 0 22 22"><circle cx="11" cy="11" r="11" fill="#2e4aa0"/><rect x="7.5" y="4.5" width="7" height="13" rx="1.5" fill="none" stroke="#fff" stroke-width="1.6"/><circle cx="11" cy="15" r="0.9" fill="#fff"/></svg>
        <span>Mobile: 0491 570 156</span>
      </li>
      <li>
        <svg class="ico" viewBox="0 0 22 22"><circle cx="11" cy="11" r="11" fill="#2e4aa0"/><path d="M7 6c1-1 2 0 2.5 1.5s-.8 1.8-.5 2.6 1.6 2.4 2.4 2.7 1.1-.9 2.6-.4 2.3 1.5 1.3 2.5-3 1-5.3-1.3S5.8 7.2 7 6z" fill="#fff"/></svg>
        <span>Office: 5900 4418</span>
      </li>
      <li>
        <svg class="ico" viewBox="0 0 22 22"><circle cx="11" cy="11" r="11" fill="#2e4aa0"/><rect x="5" y="7" width="12" height="8" fill="none" stroke="#fff" stroke-width="1.5"/><path d="M5 7l6 5 6-5" fill="none" stroke="#fff" stroke-width="1.5"/></svg>
        <span>dean@harbenrealestate.com.au</span>
      </li>
      <li>
        <svg class="ico" viewBox="0 0 22 22"><circle cx="11" cy="11" r="11" fill="#2e4aa0"/><circle cx="11" cy="11" r="6" fill="none" stroke="#fff" stroke-width="1.4"/><path d="M5 11h12M11 5c-3 3-3 9 0 12M11 5c3 3 3 9 0 12" fill="none" stroke="#fff" stroke-width="1.2"/></svg>
        <span class="web">www.harbenrealestate.com.au</span>
      </li>
      <li>
        <svg class="ico" viewBox="0 0 22 22"><circle cx="11" cy="11" r="11" fill="#2e4aa0"/><path d="M11 4.5a4.5 4.5 0 0 1 4.5 4.5c0 3.2-4.5 8.5-4.5 8.5S6.5 12.2 6.5 9A4.5 4.5 0 0 1 11 4.5z" fill="#fff"/><circle cx="11" cy="9" r="1.7" fill="#2e4aa0"/></svg>
        <span>Shop 4, 12 Tidewater Grove, Seabrook</span>
      </li>
    </ul>
  </section>

  <!-- BACK -->
  <section class="panel back" aria-label="Flyer back">
    <div class="photo hero" role="img" aria-label="Dusk photo of a sold single-storey home with timber garage door"></div>
    <div class="abs sold-band">SOLD</div>
    <div class="photo p-deck" role="img" aria-label="Photo of a covered timber deck looking out to the beach"></div>
    <div class="photo p-dusk" role="img" aria-label="Sunset photo of a lit home among palm trees"></div>
    <div class="photo p-lawn" role="img" aria-label="Photo of a brick home behind a green front lawn"></div>
    <div class="photo p-room" role="img" aria-label="Photo of a bright living room with a black sofa"></div>
    <div class="photo p-drive" role="img" aria-label="Photo of a paved garden path leading to a home"></div>
  </section>

</div>
</body>
</html>
```